Spiritual journeyer, astrologer, Reiki master, underground music lover needs business card design

Initially I need a business card design (and possibly a logo for my new website). I offer astrological and energetic inquiry and guidance to clients in support of their life's evolutionary path. I combine an eclectic mix of methods with a focus on the mind body connection. I am a spiritual journeyer, astrologer, Reiki Master, certified personal trainer, soon to be black belt in Taekwondo (karate), and researcher into the benefits of music/sound vibrational therapy. And underground music lover :) The attached drawing is just something I drew freehand, it is symbolic of many things important to me. I wanted the figure to clearly be female. Her arms are open to catch the sky, the name of my new business is Orlabrook, and Orla is my daughter's name. This was just an idea I had, I'm open to suggestions. The photo is me with the planets in the sky as they were at the moment I was born (some years ago-LOL)
Updates

I have picked a final design. Thank you everyone for your time and effort.

Target Market(s)

Worldwide, what I do can be done in person or anywhere in the world via Skype

Industry/Entity Type

Professional Service

Contact Information for Business Card

Simple, unusual image with my business name and contact info

Font styles to use
Sans Serif

Requirements
Must have
• My website very clean, simple. Somehow combine biz name of Orlabrook with female figure catching/holding the starry sky? See my poor drawing I attached.
Nice to have
• Something that conveys all the unique, unusual, eclectic skills and capacities I have
Should not have
• Frilly, fancy, stuffy

```html
<!DOCTYPE html>
<html lang="en">
<head>
<meta charset="utf-8">
<title>Orlabrook – Business Card</title>
<link href="https://fonts.googleapis.com/css2?family=Open+Sans:wght@400;600&display=swap" rel="stylesheet">
<style>
  :root {
    --bg: #000000;
    --card: #2f3034;
    --ink: #ffffff;
    --ink-soft: #e8e8ea;
    --rule: #3c3d42;
  }
  * { margin: 0; padding: 0; box-sizing: border-box; }
  html, body {
    width: 1200px; height: 900px; overflow: hidden;
    background: var(--bg);
    font-family: "Open Sans", Arial, sans-serif;
    color: var(--ink);
  }
  .stage { position: relative; width: 1200px; height: 900px; }
  .card {
    position: absolute;
    background: var(--card);
    border-radius: 14px;
  }
  .card--front { left: 137px; top: 270px; width: 457px; height: 283px; }
  .card--back  { left: 626px; top: 270px; width: 458px; height: 282px; }

  .brand-mark {
    position: absolute;
    border: 5px solid var(--ink);
    border-radius: 50%;
    display: flex; align-items: center; justify-content: center;
  }
  .card--front .brand-mark { left: 63px; top: 71px; width: 134px; height: 134px; }
  .brand-mark__name { font-size: 17px; font-weight: 600; color: var(--ink); }

  .divider {
    position: absolute; left: 226px; top: 80px;
    width: 1px; height: 116px; background: var(--rule);
  }
  .details { position: absolute; left: 250px; top: 77px; }
  .details__name { font-size: 16px; font-weight: 600; line-height: 22px; }
  .details__role { font-size: 12.5px; line-height: 19px; color: var(--ink-soft); margin-top: 1px; }
  .contact { list-style: none; margin-top: 14px; }
  .contact__item {
    display: flex; align-items: center;
    font-size: 12.5px; line-height: 19px; color: var(--ink-soft);
  }
  .contact__icon { width: 9px; height: 9px; margin: 0 8px 0 1px; fill: var(--ink-soft); }

  .card--back .brand-mark { left: 157px; top: 61px; width: 112px; height: 112px; border-width: 4px; }
  .wordmark {
    position: absolute; left: 0; right: 0; top: 172px;
    text-align: center;
    font-size: 40px; font-weight: 600; letter-spacing: 0.2px;
    color: var(--ink);
  }
</style>
</head>
<body>
<main class="stage">
  <section class="card card--front">
    <div class="brand-mark"><span class="brand-mark__name">Orlabrook</span></div>
    <div class="divider"></div>
    <div class="details">
      <h1 class="details__name">Maren Holloway</h1>
      <p class="details__role">Astrological and Energetic<br>Guidance and Inquiry</p>
      <ul class="contact">
        <li class="contact__item">
          <svg class="contact__icon" viewBox="0 0 10 10"><path d="M2 0.5 L3.6 2.6 L2.7 3.6 C3.3 5 4.9 6.7 6.4 7.3 L7.4 6.4 L9.5 8 L8.4 9.5 C4.5 9.2 0.8 5.5 0.5 1.6 Z"/></svg>
          555-014-272
        </li>
        <li class="contact__item">
          <svg class="contact__icon" viewBox="0 0 10 10"><path d="M0.5 2 H9.5 V8.5 H0.5 Z M1 2.4 L5 5.6 L9 2.4" fill="none" stroke="#e8e8ea" stroke-width="1"/><path d="M0.5 2 H9.5 L5 5.5 Z"/></svg>
          info@orlabrook.com
        </li>
        <li class="contact__item">
          <svg class="contact__icon" viewBox="0 0 10 10"><circle cx="5" cy="5" r="4.5"/><path d="M5 0.5 V9.5 M0.5 5 H9.5" stroke="#2f3034" stroke-width="0.8"/></svg>
          www.orlabrook.com
        </li>
      </ul>
    </div>
  </section>

  <section class="card card--back">
    <div class="brand-mark"></div>
    <h2 class="wordmark">Orlabrook</h2>
  </section>
</main>
</body>
</html>
```